Elegant YET Modern - Business Card Design

I need a business card for my real estate consulting business. I am hired by developers to create and manage marketing and sales programs for their high-end, multi-unit real estate developments. These projects can last a few years. My clients are fast-moving, affluent, no nonsense men (mostly). I need a card that is elegant yet modern, understated yet with a creative touch. Less is more! Colors need to be sophisticated...charcoal grey/white or I'm open.
I would like my tagline: "Elevate Your Real Estate. Accelerate Your Sales." on the back of card with a simple skyline illustration (hopefully I can get the skyline spot colored)...see attached sample
I don't have a logo yet so simple clean chic is good start. I D NOT want a bunch of "Stars" in a row as too predictable. But an interesting treatment of stars in or around logo type could be great.
The FINAL design should communicate: modern elegance, confidence, and restraint

Target Market(s)

affluent male real estate developers between 45-70 - confident, succesful, busy, results oriented

Industry/Entity Type

Real Estate

Contact Information for Business Card

Silver Crest Marketing
Elevate Your Real Estate. Accelerate Your Sales.

Rachel Dunwoody
President
208.555.0173
Rachel@crestvalemkt.com

Requirements
Must have
• The name "Silver Crest Marketing" is a play on the star rating system for hotels and resorts...(and indicates the types of projects I work on) ...if there is a Star or Stars in your design (and I would love it) the treatment of the Star/s should imply sophistication (either modern or understated)...but not contrived or cheap looking.

I also like the idea of a reference to real estate...can be the simple skyline rendering but I'm open to other suggestions...should NOT BE a single home or roof top as I DO NOT sell single family residential homes...I AM NOT a real estate agent!!!

```html
<!DOCTYPE html>
<html lang="en">
<head>
<meta charset="utf-8">
<title>Silver Crest Marketing – Business Card</title>
<link rel="stylesheet" href="https://fonts.googleapis.com/css2?family=Montserrat:wght@500;600;700&family=Open+Sans:wght@300;400&display=swap">
<style>
  :root {
    --charcoal: #1f1e23;
    --paper: #ffffff;
    --accent-red: #ea2127;
    --muted: #cfcfd2;
    --backdrop: #ece9e4;
    --tab-shadow: rgba(0,0,0,0.25);
    --card-shadow: rgba(0,0,0,0.22);
  }
  * { margin: 0; padding: 0; box-sizing: border-box; }
  html, body { width: 1200px; height: 903px; overflow: hidden; }
  body { background: var(--backdrop); position: relative; font-family: "Open Sans", sans-serif; }

  .card {
    position: absolute; width: 560px; height: 320px; overflow: hidden;
    background: var(--charcoal);
    box-shadow: 0 10px 28px var(--card-shadow);
  }
  .card--front { left: 90px; top: 100px; }
  .card--back { left: 550px; top: 480px; }

  .panel-white { position: absolute; left: 0; top: 0; bottom: 0; background: var(--paper); }
  .card--front .panel-white { width: 190px; }
  .card--back .panel-white { width: 200px; }

  .band {
    position: absolute; top: 0; width: 24px; background: var(--accent-red);
    border-radius: 0 0 8px 8px;
  }
  .card--front .band--divider { left: 190px; height: 290px; }
  .card--front .band--icons { left: 500px; height: 262px; }
  .card--back .band--divider { left: 200px; height: 296px; }

  .tab {
    position: absolute; background: var(--paper); border-radius: 5px;
    box-shadow: 0 3px 5px var(--tab-shadow);
  }
  .tab--plain { width: 36px; height: 28px; }
  .tab--icon { width: 40px; height: 36px; display: flex; align-items: center; justify-content: center; }
  .tab--icon svg { width: 22px; height: 22px; }

  .brand {
    position: absolute; left: 0; top: 124px; width: 190px; text-align: center;
    font-family: "Montserrat", sans-serif; font-weight: 700; font-size: 17px;
    line-height: 1.25; color: var(--charcoal);
  }
  .brand__rule { display: block; width: 110px; height: 1px; background: var(--accent-red); margin: 10px auto 0; }
  .brand__mark { display: block; width: 8px; height: 8px; background: var(--accent-red); margin: 10px auto 0; }

  .contact {
    position: absolute; right: 82px; text-align: right; color: var(--paper);
  }
  .contact__rule { display: block; height: 1px; background: var(--accent-red); margin-left: auto; margin-top: 8px; }
  .contact--name { top: 34px; }
  .contact__name { font-family: "Montserrat", sans-serif; font-weight: 700; font-size: 16px; line-height: 1.2; }
  .contact__title { font-family: "Open Sans", sans-serif; font-weight: 400; font-size: 12px; color: var(--muted); }
  .contact--name .contact__rule { width: 100px; }
  .contact--phone { top: 130px; font-size: 14px; font-weight: 300; }
  .contact--phone .contact__rule { width: 110px; }
  .contact--email { top: 210px; font-size: 13px; font-weight: 300; }
  .contact--email .contact__rule { width: 110px; }

  .skyline {
    position: absolute; left: 26px; top: 46px; width: 160px; height: 250px;
    background: linear-gradient(180deg, #b9cbe0 0%, #7f97b3 55%, #4d5f78 100%);
    border-radius: 3px;
  }

  .tagline {
    position: absolute; left: 224px; right: 0; top: 118px; text-align: center;
    font-family: "Montserrat", sans-serif; font-weight: 600; font-size: 20px;
    line-height: 1.5; color: var(--paper);
  }
</style>
</head>
<body>

  <section class="card card--front" aria-label="Business card front">
    <div class="panel-white"></div>
    <div class="band band--divider"></div>
    <div class="tab tab--plain" style="left:184px; top:150px;"></div>

    <div class="brand">
      Silver Crest<br>Marketing
      <span class="brand__rule"></span>
      <span class="brand__mark" aria-hidden="true"></span>
    </div>

    <div class="contact contact--name">
      <div class="contact__name">Rachel Dunwoody</div>
      <div class="contact__title">President</div>
      <span class="contact__rule"></span>
    </div>
    <div class="contact contact--phone">
      208.555.0173
      <span class="contact__rule"></span>
    </div>
    <div class="contact contact--email">
      Rachel@crestvalemkt.com
      <span class="contact__rule"></span>
    </div>

    <div class="band band--icons"></div>
    <div class="tab tab--icon" style="left:492px; top:36px;">
      <svg viewBox="0 0 24 24" aria-hidden="true"><rect x="2" y="2" width="20" height="20" fill="#1f1e23"/><circle cx="12" cy="9" r="4" fill="#fff"/><path d="M4 22c0-5 3.5-7 8-7s8 2 8 7z" fill="#fff"/></svg>
    </div>
    <div class="tab tab--icon" style="left:492px; top:118px;">
      <svg viewBox="0 0 24 24" aria-hidden="true"><rect x="6" y="1.5" width="12" height="21" rx="2" fill="none" stroke="#1f1e23" stroke-width="1.8"/><line x1="10" y1="19" x2="14" y2="19" stroke="#1f1e23" stroke-width="1.6"/></svg>
    </div>
    <div class="tab tab--icon" style="left:492px; top:200px;">
      <svg viewBox="0 0 24 24" aria-hidden="true"><rect x="2" y="3" width="20" height="14" rx="1" fill="none" stroke="#1f1e23" stroke-width="2"/><line x1="12" y1="17" x2="12" y2="20" stroke="#1f1e23" stroke-width="2"/><line x1="7" y1="21" x2="17" y2="21" stroke="#1f1e23" stroke-width="2"/></svg>
    </div>
  </section>

  <section class="card card--back" aria-label="Business card back">
    <div class="panel-white">
      <div class="skyline" role="img" aria-label="Illustration of glass high-rise towers forming a city skyline"></div>
    </div>
    <div class="band band--divider"></div>
    <div class="tab tab--plain" style="left:194px; top:50px;"></div>
    <div class="tab tab--plain" style="left:194px; top:140px;"></div>
    <div class="tab tab--plain" style="left:194px; top:230px;"></div>

    <p class="tagline">Elevate Your Real Estate<br>Accelerate Your Sales</p>
  </section>

</body>
</html>
```